Property Developer - Simple yet Sophisticated and Sharp Business Card

We are a medium sized property developer involved mainly in townhouse developments and land subdivisions.

The company is looking for a simple, sharp and sophisticated business card that will be given to contractors, land owners, financiers etc and thus will need to look professional.

Property development related graphics and art can be used, however the card is not to be too "busy" or crowded. Our company name is KL Estates which could possibly be incorporated into the graphics or artwork.

Single sided and/or double sided designs will be acceptable.

A Simple, Sophisticated, Sharp design please!

Good Luck !

```html
<!DOCTYPE html>
<html lang="en">
<head>
<meta charset="utf-8">
<title>KL Estates – Business Card</title>
<link rel="stylesheet" href="https://fonts.googleapis.com/css2?family=Open+Sans:wght@400;600;700&display=swap">
<style>
  :root {
    --page: #ffffff;
    --card-edge: #b9b9b9;
    --brand-green: #8dc63f;
    --ink: #111111;
    --white: #ffffff;
    --bar-light: #f7f7f7;
    --bar-mid: #ececec;
    --bar-dark: #e2e2e2;
    --tower-dark: #1a1a1a;
    --tower-light: #e9e9e9;
  }
  * { margin: 0; padding: 0; box-sizing: border-box; }
  html, body {
    width: 1200px;
    height: 721px;
    overflow: hidden;
    background: var(--page);
  }
  .card {
    position: absolute;
    left: 38px;
    top: 38px;
    width: 1122px;
    height: 639px;
    background: var(--white);
    border: 2px solid var(--card-edge);
    font-family: "Open Sans", Arial, sans-serif;
    color: var(--ink);
    overflow: hidden;
  }
  .brand-band {
    position: absolute;
    left: 0;
    top: 0;
    width: 100%;
    height: 238px;
    background: var(--brand-green);
  }
  .company-name {
    position: absolute;
    left: 56px;
    top: 70px;
    font-size: 56px;
    font-weight: 700;
    color: var(--white);
    letter-spacing: 0.5px;
    line-height: 1;
  }
  .skyline-art {
    position: absolute;
    left: 830px;
    top: 58px;
    width: 240px;
    height: 214px;
  }
  .person {
    position: absolute;
    right: 596px;
    text-align: right;
    line-height: 1;
  }
  .person-name {
    top: 330px;
    font-size: 46px;
  }
  .person-role {
    top: 398px;
    font-size: 38px;
  }
  .contact-lines {
    position: absolute;
    left: 662px;
    top: 340px;
    font-size: 28px;
    line-height: 54px;
  }
  .email-bar {
    position: absolute;
    left: 0;
    top: 518px;
    width: 100%;
    height: 46px;
    background: linear-gradient(to right, var(--bar-light) 0%, var(--bar-mid) 18%, var(--white) 38%, var(--white) 100%);
  }
  .email-bar::after {
    content: "";
    position: absolute;
    left: 452px;
    top: 0;
    right: 0;
    bottom: 0;
    background: var(--bar-dark);
  }
  .email-line {
    position: absolute;
    left: 488px;
    top: 522px;
    font-size: 29px;
    line-height: 38px;
    z-index: 1;
  }
  .postal-line {
    position: absolute;
    left: 0;
    width: 100%;
    top: 580px;
    text-align: center;
    font-size: 30px;
    line-height: 40px;
  }
</style>
</head>
<body>
  <div class="card">
    <div class="brand-band"></div>
    <h1 class="company-name">KL Estates</h1>

    <svg class="skyline-art" viewBox="0 0 240 214" role="img" aria-label="Illustration of three black and white high-rise buildings">
      <defs>
        <linearGradient id="towerTone" x1="0" y1="0" x2="1" y2="0">
          <stop offset="0" stop-color="var(--tower-dark)"/>
          <stop offset="0.5" stop-color="var(--tower-light)"/>
          <stop offset="1" stop-color="var(--tower-dark)"/>
        </linearGradient>
      </defs>
      <rect x="0" y="0" width="240" height="214" fill="url(#towerTone)"/>
    </svg>

    <p class="person person-name">employee name</p>
    <p class="person person-role">job title</p>

    <div class="contact-lines">
      <p class="contact-phone">Phone: (07) 3204 5186</p>
      <p class="contact-fax">Fax: (07) 3204 5187</p>
    </div>

    <div class="email-bar"></div>
    <p class="email-line">Email: projects.klestates@mail.com</p>

    <p class="postal-line">Postal: PO Box 2745 Parkwood Heights QLD 4127</p>
  </div>
</body>
</html>
```